Business Card design for Property Developer

We need a business card design for a Melbourne based Property Developer called "Kestrelmoor Holdings Pty Ltd".

We subdivide land and onsell to builders etc.

We already have a company logo, which is attached. Also I have attached the layout requirements from the printer. We would like a 2-sided design with one side displaying our logo by itself and the other with the required info, such as name, address, tel no., email, abn etc. The card will need to be used by 4 members of staff so name and contact details should be interchangable.
Updates

If possible, can you please write "name' "job position" "phone" "email" "address" on the card but leave them so I can add the details at a later time. Thank you. Also I plan on printing with UV spot printing as a background on the card. Keep this is mind when designing.

Thanks again.

Hello designers, please do not include pics of houses, house plansĀ or construction machinery etc as we really do not like the way it looks. Thank you.

Target Market(s)

Real Estate Agents, Land Owners, Local Council Departments, Govt Bodies, other Developers etc.

Industry/Entity Type

Business

Requirements
Must have
• 2-sided design with one side displaying our logo by itself and the other with the required info, such as name, address, tel no., email, abn etc.

```html
<!DOCTYPE html>
<html lang="en">
<head>
<meta charset="utf-8">
<title>Kestrelmoor Holdings Pty Ltd — Business Card, Info Side</title>
<link rel="stylesheet" href="https://fonts.googleapis.com/css2?family=Questrial&family=Montserrat:wght@700&display=swap">
<style>
  :root {
    --blue-deep: #0718d8;
    --blue-mid: #1650f0;
    --blue-light: #3ec6ff;
    --mark-tone: #1a38e6;
    --mark-edge: #0b22c4;
    --text: #ffffff;
  }
  * { margin: 0; padding: 0; box-sizing: border-box; }
  html, body {
    width: 1200px;
    height: 783px;
    overflow: hidden;
    background: #ffffff;
  }
  .card {
    position: relative;
    width: 1200px;
    height: 783px;
    overflow: hidden;
    color: var(--text);
    font-family: "Questrial", "Century Gothic", sans-serif;
    background: linear-gradient(62deg, var(--blue-light) 0%, #2a8ff8 30%, var(--blue-mid) 55%, var(--blue-deep) 85%);
  }
  .brand-mark-area {
    position: absolute;
    left: 800px;
    top: 90px;
    width: 560px;
    height: 760px;
    border-radius: 50%;
    background: radial-gradient(circle at 45% 48%, var(--mark-edge) 0%, var(--mark-tone) 45%, rgba(26, 56, 230, 0.35) 70%, rgba(26, 56, 230, 0) 80%);
  }
  .address {
    position: absolute;
    left: 108px;
    top: 330px;
    font-size: 30px;
    line-height: 39px;
  }
  .contacts {
    position: absolute;
    left: 108px;
    top: 536px;
    font-size: 28px;
    line-height: 39px;
    letter-spacing: 0.5px;
  }
  .contacts .label {
    font-family: "Montserrat", "Century Gothic", sans-serif;
    font-weight: 700;
  }
  .person {
    position: absolute;
    right: 112px;
    top: 558px;
    text-align: right;
  }
  .person .name {
    font-family: "Montserrat", "Century Gothic", sans-serif;
    font-weight: 700;
    font-size: 46px;
    line-height: 54px;
  }
  .person .role {
    font-size: 31px;
    line-height: 40px;
  }
</style>
</head>
<body>
  <main class="card">
    <div class="brand-mark-area" role="img" aria-label="Large partial Kestrelmoor Holdings logo symbol as background decoration"></div>

    <p class="address">
      address address<br>
      addressaddressaddress<br>
      addressaddress<br>
      address
    </p>

    <p class="contacts">
      <span class="label">Tel:</span> ??? ??? ????<br>
      <span class="label">Email:</span> ??????@?????????????<br>
      <span class="label">ABN:</span> ?? ??? ??? ???
    </p>

    <div class="person">
      <p class="name">name</p>
      <p class="role">job position</p>
    </div>
  </main>
</body>
</html>
```